Business Card for By Karel Voss

Looking to have a business card designed for my lifestyle and fitness company. My company offers personal training, online programming and nutrition advice based out of London, United Kingdom.

I'd like to see modern, sleek designs, focusing on black, matte black or matte grey. Design doesn't need to be overly descriptive as this will also be used as a personal business card. I've included my logo.

Please note that my company is no longer called "By Karel Voss" but instead "By Karel Voss", this is because of my other ventures. Therefore please don't use the "fitness by karel voss" text.

information about my company can be found at www.bykarelvoss.com

Company is also based out of London (United Kingdom) & Sydney (Australia) this could be reflected on the card.

Industry/Entity Type

Business

Contact Information for Business Card

Karel Voss
+44 7382 615027
karel@bykarelvoss.com
www.bykarelvoss.com

Font styles to use
Sans Serif

Requirements
Must have
• All contact details and inclusion of my logo.

```html
<!DOCTYPE html>
<html lang="en">
<head>
<meta charset="UTF-8">
<title>Karel Voss – Business Card</title>
<link rel="stylesheet" href="https://fonts.googleapis.com/css2?family=Oswald:wght@700&family=Jost:wght@400&display=swap">
<style>
  :root {
    --backdrop: #1c1c1c;
    --card-front: #5b595a;
    --card-back: #ffffff;
    --ink: #1a1a1a;
    --ink-soft: #333333;
    --on-dark: #ffffff;
  }
  * { box-sizing: border-box; margin: 0; padding: 0; }
  html, body { width: 1200px; height: 1000px; overflow: hidden; }
  body { background: var(--backdrop); position: relative; }

  .card {
    position: absolute;
    width: 580px;
    height: 330px;
    border-radius: 28px;
    box-shadow: 0 12px 30px rgba(0,0,0,0.6);
  }

  /* Front side */
  .card-front {
    left: 130px; top: 110px;
    background: var(--card-front);
    display: flex; align-items: center; justify-content: center;
  }
  .front-wordmark {
    font-family: "Oswald", sans-serif;
    font-weight: 700;
    color: var(--on-dark);
    text-transform: uppercase;
    text-align: center;
    line-height: 1;
  }
  .front-wordmark .line-small { display: block; font-size: 34px; letter-spacing: 2px; }
  .front-wordmark .line-large { display: block; font-size: 66px; letter-spacing: 3px; margin-top: 6px; }

  /* Back side */
  .card-back {
    left: 490px; top: 540px;
    background: var(--card-back);
    display: flex; align-items: center;
    padding: 0 40px 0 44px;
  }
  .brand {
    width: 210px;
    display: flex; flex-direction: column; align-items: center;
  }
  .brand-mark {
    width: 74px; height: 74px;
    border-radius: 50%;
    background: var(--ink);
    margin-bottom: 18px;
  }
  .brand-name {
    font-family: "Oswald", sans-serif;
    font-weight: 700;
    color: var(--ink);
    text-transform: uppercase;
    text-align: center;
    line-height: 1.05;
  }
  .brand-name .line-small { display: block; font-size: 17px; letter-spacing: 1px; }
  .brand-name .line-large { display: block; font-size: 30px; letter-spacing: 1.5px; }

  .divider {
    width: 2px; height: 210px;
    background: var(--ink);
    margin: 0 26px 0 28px;
  }

  .details { font-family: "Jost", sans-serif; color: var(--ink-soft); }
  .person-name {
    font-family: "Oswald", sans-serif;
    font-weight: 700;
    font-size: 30px;
    color: var(--ink);
    letter-spacing: 0.5px;
    line-height: 1;
  }
  .person-role { font-size: 14px; margin-top: 4px; letter-spacing: 0.5px; }
  .address { font-size: 13px; line-height: 1.35; margin-top: 22px; }
  .contact-list { list-style: none; margin-top: 8px; }
  .contact-list li {
    display: flex; align-items: center;
    font-size: 13px; line-height: 1.6;
  }
  .contact-list svg { width: 12px; height: 12px; margin-right: 8px; fill: var(--ink); flex: none; }
</style>
</head>
<body>

  <section class="card card-front" aria-label="Card front">
    <div class="front-wordmark">
      <span class="line-small">By</span>
      <span class="line-large">Karel Voss</span>
    </div>
  </section>

  <section class="card card-back" aria-label="Card back">
    <div class="brand">
      <div class="brand-mark"></div>
      <div class="brand-name">
        <span class="line-small">By</span>
        <span class="line-large">Karel Voss</span>
      </div>
    </div>

    <div class="divider"></div>

    <div class="details">
      <h1 class="person-name">KAREL VOSS</h1>
      <p class="person-role">CEO &amp; FOUNDER</p>
      <p class="address">London, United Kingdom<br>Sydney, Australia</p>
      <ul class="contact-list">
        <li>
          <svg viewBox="0 0 24 24" aria-hidden="true"><path d="M6.6 10.8a15.1 15.1 0 0 0 6.6 6.6l2.2-2.2a1 1 0 0 1 1-.25 11.4 11.4 0 0 0 3.6.57 1 1 0 0 1 1 1V20a1 1 0 0 1-1 1A17 17 0 0 1 3 4a1 1 0 0 1 1-1h3.5a1 1 0 0 1 1 1c0 1.250.2 2.45.57 3.6a1 1 0 0 1-.25 1z"/></svg>
          +44 7382 615027
        </li>
        <li>
          <svg viewBox="0 0 24 24" aria-hidden="true"><path d="M2 5h20v14H2z M2 5l10 8 10-8" stroke="#fff" stroke-width="1.6"/></svg>
          karel@bykarelvoss.com
        </li>
        <li>
          <svg viewBox="0 0 24 24" aria-hidden="true"><circle cx="14" cy="10" r="7" fill="none" stroke="#1a1a1a" stroke-width="2.6"/><path d="M9 15l-6 6" stroke="#1a1a1a" stroke-width="2.6"/></svg>
          www.bykarelvoss.com
        </li>
      </ul>
    </div>
  </section>

</body>
</html>
```